Flyer / Mailer for Business Debt Relief Business - Harborline Relief 6" x 11"

We need a 6" x 11" double sided flyer. This will be sent out to potential customers with high interest business loans. We would like the design to coordinate with the colors of our logo. I have included a mock up that we sketched out. I have also included a file of a mailer we received that we would like to use as a template (not colors or fonts, just set up). I have also included an .ai file of our logo.

```html
<!DOCTYPE html>
<html lang="en">
<head>
<meta charset="UTF-8">
<title>Harborline Relief – Business Debt Relief Mailer</title>
<link href="https://fonts.googleapis.com/css2?family=Arimo:wght@400;700&display=swap" rel="stylesheet">
<style>
  :root {
    --brand-blue: #2273b9;
    --deep-blue: #1d5d9c;
    --header-grey: #e7e8e9;
    --band-grey: #d3d5d7;
    --footer-grey: #dddee0;
    --green-dark: #4f9f35;
    --green-mid: #6db443;
    --green-light: #a6d177;
    --white: #ffffff;
    --logo-green: #4ca64a;
  }
  * { margin: 0; padding: 0; box-sizing: border-box; }
  html, body { width: 1200px; height: 655px; overflow: hidden; background: var(--white); }
  body { font-family: "Arimo", Arial, sans-serif; }

  .mailer { position: relative; width: 1200px; height: 655px; overflow: hidden; background: var(--header-grey); }

  /* left photo column */
  .photo { position: absolute; left: 0; width: 270px; }
  .photo--savings-board { top: 0; height: 187px; background: linear-gradient(135deg, #6b4a33 0%, #3e4a4c 45%, #2f3a3b 70%, #8a6a4d 100%); }
  .photo--piggy-bank { top: 189px; height: 324px; background: linear-gradient(160deg, #f4f1ee 0%, #ead9d6 45%, #f2c9c6 70%, #e9e6e3 100%); }
  .photo--coin-growth { top: 515px; height: 140px; background: linear-gradient(90deg, #c9d9a8 0%, #e6e3cf 40%, #f3dcd6 70%, #dfe6c4 100%); }

  /* header */
  .header { position: absolute; left: 270px; top: 0; width: 930px; height: 118px; background: var(--header-grey); }
  .headline { position: absolute; left: 25px; top: 52px; font-size: 24px; font-weight: 700; color: var(--brand-blue); letter-spacing: -0.1px; }
  .brand { position: absolute; right: 22px; top: 28px; display: flex; flex-direction: column; align-items: center; gap: 8px; }
  .brand__mark { width: 44px; height: 44px; background: var(--logo-green); }
  .brand__name { font-size: 16px; font-weight: 400; color: #3a3a3a; letter-spacing: 1px; text-transform: uppercase; }

  .intro-band { position: absolute; left: 270px; top: 118px; width: 930px; height: 69px; background: var(--band-grey); }
  .intro-band p { position: absolute; left: 25px; top: 23px; font-size: 20px; color: var(--brand-blue); }

  /* green offer panel */
  .offer { position: absolute; left: 270px; top: 187px; width: 930px; height: 328px;
    background: linear-gradient(90deg, var(--green-dark) 0%, var(--green-mid) 45%, var(--green-light) 62%, #c9dfc0 72%, #c5d3de 82%, #9fb3c8 100%); }
  .photo--consultant { position: absolute; left: 520px; top: 0; width: 410px; height: 328px;
    background: linear-gradient(90deg, rgba(166,209,119,0) 0%, rgba(120,150,185,0.45) 40%, rgba(40,62,110,0.75) 70%, rgba(215,222,230,0.6) 100%); }
  .offer__title { position: absolute; left: 25px; top: 29px; font-size: 19px; font-weight: 700; color: var(--white); }
  .benefits { position: absolute; left: 25px; top: 72px; list-style: none; }
  .benefits li { font-size: 14.5px; color: var(--white); line-height: 29.5px; }
  .benefits li::before { content: "•"; margin-right: 6px; }

  /* contact footer */
  .contact { position: absolute; left: 270px; top: 515px; width: 930px; height: 140px; background: var(--footer-grey);
    text-align: center; color: var(--deep-blue); font-weight: 700; font-size: 19px; padding-top: 14px; }
  .contact p { line-height: 28px; }
  .contact .phone { font-size: 20px; }
</style>
</head>
<body>
<main class="mailer">
  <div class="photo photo--savings-board" role="img" aria-label="Chalkboard reading 'Time to save money' beside a coffee cup"></div>
  <div class="photo photo--piggy-bank" role="img" aria-label="Hand dropping a coin into a pink piggy bank"></div>
  <div class="photo photo--coin-growth" role="img" aria-label="Stacks of coins growing beside a small piggy bank"></div>

  <header class="header">
    <h1 class="headline">Helping Businesses Focus on What Matters!</h1>
    <div class="brand">
      <span class="brand__mark"></span>
      <span class="brand__name">Harborline Relief</span>
    </div>
  </header>

  <div class="intro-band">
    <p>We understand that merchant cash advance loans can be a burden on your business</p>
  </div>

  <section class="offer">
    <div class="photo--consultant" role="img" aria-label="Businessman in a suit gesturing at a desk with papers"></div>
    <h2 class="offer__title">Overwhelmed by daily/weekly payments? WE CAN HELP!</h2>
    <ul class="benefits">
      <li>This is not a loan, WE ARE NOT LENDERS!</li>
      <li>Improve your business's cash flow immediately</li>
      <li>Reduce the amount you are paying out monthly</li>
      <li>Strategic alternatives to high interest loans</li>
      <li>Fast, confidential business debt relief</li>
      <li>No-obligation consultation</li>
      <li>Absolutely no credit pulls</li>
      <li>No collateral, no financials</li>
    </ul>
  </section>

  <footer class="contact">
    <p>Visit Our Website: www.harborlinerelief.com</p>
    <p>Call Now For Free Condultation With Our Experts</p>
    <p class="phone">844 - 555 - 0172</p>
    <p>Email: info@harborlinerelief.com</p>
  </footer>
</main>
</body>
</html>
```